Business Card for Managing Partner Investment Fund

To create a business card template for an investment fund manager. Business card should be more professional in nature, not too colorful, more upscale, and created using the attached logos and fund name files. I would prefer a black or gray color scheme, but am open to the use of color as well. I would prefer a double sided business card, but open to single sided business card designs as well. The business card should include: name, title, and contact information, as well as logo and company name. I would prefer a more stream-lined, simple business card design.
Updates
Address: 4190 NE 38th Ter. Ocala, FL 34470
Email: talvin47@quorimail.net
Phone: 561-347-9162
Title: managing partner
Name: Dorian Velsky
Fund Name: Ambergate Capital
Logos can be found in files attached to the brief
Target Market(s)
potential investors, other fund managers
Industry/Entity Type
Finance
Contact Information for Business Card
Name on card: Dorian Velsky
Title: Managing Partner
Colors
Designer to choose colors to be used in the design.
Requirements
Must have
- Phone number
- email address
- physical address
- title
- name
- logo
- Fund name
Nice to have
- simple layout
Should not have
- too many colors, busy fonts,

```html
<!DOCTYPE html>
<html lang="en">
<head>
<meta charset="utf-8">
<title>Ambergate Capital — Business Card</title>
<link rel="stylesheet" href="https://fonts.googleapis.com/css2?family=Roboto:wght@400;500&display=swap">
<style>
  :root {
    --backdrop: #e9e8e6;
    --card-front: #ffffff;
    --card-back: #5b5b5b;
    --ink-strong: #2b2b2b;
    --ink: #4a4a4a;
    --brand-grey: #5a5a5a;
    --on-dark: #ffffff;
  }
  * { margin: 0; padding: 0; box-sizing: border-box; }
  html, body {
    width: 1200px; height: 1200px; overflow: hidden;
    background: var(--backdrop);
    font-family: "Roboto", Arial, sans-serif;
  }
  .canvas { position: relative; width: 1200px; height: 1200px; }
  .card {
    position: absolute; left: 213px; width: 774px; height: 442px;
    box-shadow: 0 6px 18px rgba(0,0,0,0.18);
  }
  .card--front { top: 150px; background: var(--card-front); }
  .card--back { top: 633px; background: var(--card-back); }

  .brand-name {
    position: absolute; left: 43px; top: 112px;
    color: var(--brand-grey); font-weight: 400;
    text-transform: uppercase; line-height: 1.1;
  }
  .brand-name__main { display: block; font-size: 40px; letter-spacing: 3px; }
  .brand-name__sub { display: block; font-size: 26px; letter-spacing: 9px; margin-top: 6px; padding-left: 76px; }

  .holder { position: absolute; right: 39px; top: 185px; text-align: right; }
  .holder__name { font-size: 30px; font-weight: 500; color: var(--ink-strong); }
  .holder__title { font-size: 20px; color: var(--ink); margin-top: 4px; }

  .address {
    position: absolute; left: 42px; top: 244px;
    font-size: 19px; line-height: 26px; color: var(--ink);
  }
  .contact-list {
    position: absolute; left: 42px; top: 310px; list-style: none;
    font-size: 19px; color: var(--ink);
  }
  .contact-list li { display: flex; align-items: center; height: 28px; }
  .contact-list svg { width: 17px; height: 17px; margin-right: 8px; flex: none; }

  .brand-name--reverse {
    position: absolute; left: 0; right: 0; top: 160px; text-align: center;
    color: var(--on-dark); font-weight: 400; text-transform: uppercase; line-height: 1.1;
  }
  .brand-name--reverse .brand-name__main { font-size: 54px; letter-spacing: 5px; }
  .brand-name--reverse .brand-name__sub { font-size: 36px; letter-spacing: 12px; margin-top: 10px; padding-left: 0; }
</style>
</head>
<body>
<main class="canvas">
  <section class="card card--front" aria-label="Card front">
    <p class="brand-name">
      <span class="brand-name__main">Ambergate</span>
      <span class="brand-name__sub">Capital</span>
    </p>

    <div class="holder">
      <p class="holder__name">Dorian Velsky</p>
      <p class="holder__title">Managing Partner</p>
    </div>

    <p class="address">4190 NE 38th Ter.<br>Ocala, FL 34470</p>

    <ul class="contact-list">
      <li>
        <svg viewBox="0 0 24 24" fill="none" stroke="#4a4a4a" stroke-width="1.6"><path d="M5 3h4l2 5-2.5 1.5a11 11 0 0 0 6 6L16 13l5 2v4a2 2 0 0 1-2 2A16 16 0 0 1 3 5a2 2 0 0 1 2-2z"/></svg>
        561-347-9162
      </li>
      <li>
        <svg viewBox="0 0 24 24" fill="none" stroke="#4a4a4a" stroke-width="1.6"><rect x="7" y="2" width="10" height="20" rx="2"/><line x1="11" y1="18" x2="13" y2="18"/></svg>
        561-347-9188
      </li>
      <li>
        <svg viewBox="0 0 24 24" fill="none" stroke="#4a4a4a" stroke-width="1.6"><rect x="3" y="5" width="18" height="14"/><path d="M3 5l9 8 9-8"/></svg>
        talvin47@quorimail.net
      </li>
      <li>
        <svg viewBox="0 0 24 24" fill="none" stroke="#4a4a4a" stroke-width="1.6"><circle cx="12" cy="12" r="9"/><ellipse cx="12" cy="12" rx="4" ry="9"/><line x1="3" y1="12" x2="21" y2="12"/></svg>
        www.ambergatecapital.net
      </li>
    </ul>
  </section>

  <section class="card card--back" aria-label="Card back">
    <p class="brand-name--reverse">
      <span class="brand-name__main">Ambergate</span>
      <span class="brand-name__sub">Capital</span>
    </p>
  </section>
</main>
</body>
</html>
```